Church needs a street sign design

We're a small church located in Silicon Valley, California. Our website is https://www.hfbmerrow.org/ and our address is 4817 Larkfield Ave, San Jose, California, 95873. You can look up our location on Google Maps to see the sign from Street View. I have uploaded an image of the street sign as well. The marquee, the top section of the sign, and the separating line between them both will be removed. We're seeking a design for a new backlit acrylic insert that will go on the front of the light box and the back of the lightbox. The acrylic sign will fill the entire external frame. In the future, we may build a decorative wood frame around the structural legs, as visualized in one of the uploaded files. The church's brand colors are: #003366 (dark blue), #ff6600 (vibrant orange), #228b22 (forest green). I have also uploaded the church's logo assets. Our primary font is Montserrat and the secondary is Poppins. You can deviate from these colors/fonts if the sign is still coherent with the rest of our branding. Our branding values are mission, truth, passion, and community (please do not put those words on the sign! They are just intended to guide the look of the design). The sign dimensions are 96" by 47.5". Keep in mind that the sign will be backlit on a busy street side. It will also be positioned next to an old-looking church building. We do NOT want a sign that looks traditional, old, or antiquated. Instead, we want a modern-looking sign that pairs well with our old building while helping it look more modern too. We would also like the web address clearly visible on the sign: hfbmerrow.org. If you have any questions, just let me know!

```html
<!DOCTYPE html>
<html lang="en">
<head>
<meta charset="utf-8">
<title>Merrow Fellowship Church – Street Sign Insert</title>
<link href="https://fonts.googleapis.com/css2?family=Montserrat:wght@700;800&family=Poppins:wght@300&display=swap" rel="stylesheet">
<style>
  :root {
    --brand-blue: #003366;
    --brand-orange: #ff6600;
    --brand-orange-warm: #ff7a12;
    --brand-green: #1f6b1f;
    --ink: #333333;
    --name-ink: #111111;
    --paper: #ffffff;
    --backdrop: #cacaca;
  }
  * { margin: 0; padding: 0; box-sizing: border-box; }
  html, body {
    width: 1200px; height: 1200px; overflow: hidden;
    background: var(--backdrop);
  }
  .canvas { position: relative; width: 1200px; height: 1200px; }
  .sign {
    position: absolute; left: 55px; top: 330px;
    width: 1090px; height: 538px;
    background: var(--paper);
    overflow: hidden;
  }
  .sign-art { position: absolute; left: 0; top: 0; width: 1090px; height: 398px; }
  .headline-line {
    position: absolute; left: 58px;
    font-family: "Montserrat", sans-serif; font-weight: 800;
    color: var(--paper); line-height: 1; white-space: nowrap;
  }
  .headline-main { font-size: 82px; letter-spacing: -0.5px; }
  .headline-making { top: 42px; }
  .headline-disciples { top: 112px; color: var(--brand-orange); }
  .headline-sub { font-size: 42px; }
  .headline-helping { top: 207px; }
  .headline-helpless { top: 252px; }
  .tagline {
    position: absolute; left: 58px; top: 312px;
    font-family: "Poppins", sans-serif; font-weight: 300;
    font-size: 46px; line-height: 1; letter-spacing: 3px;
    color: var(--paper); white-space: nowrap;
  }
  .footer-band {
    position: absolute; left: 0; top: 398px; width: 1090px; height: 140px;
  }
  .church-name {
    position: absolute; left: 64px; top: 56px;
    display: flex; align-items: center; gap: 10px;
    font-family: "Montserrat", sans-serif; font-weight: 700;
    font-size: 16px; line-height: 1; color: var(--name-ink);
    white-space: nowrap;
  }
  .church-name-mark { width: 22px; height: 22px; background: var(--name-ink); }
  .web-address {
    position: absolute; right: 82px; top: 30px;
    font-family: "Montserrat", sans-serif; font-weight: 700;
    font-size: 50px; line-height: 1; letter-spacing: 2px;
    color: var(--ink); white-space: nowrap;
  }
</style>
</head>
<body>
<div class="canvas">
  <div class="sign">
    <svg class="sign-art" viewBox="0 0 1090 398" xmlns="http://www.w3.org/2000/svg">
      <defs>
        <linearGradient id="skyBlue" x1="0" y1="0" x2="1" y2="1">
          <stop offset="0" stop-color="#023a66"/>
          <stop offset="0.55" stop-color="#0a4f86"/>
          <stop offset="1" stop-color="#003360"/>
        </linearGradient>
        <linearGradient id="sunsetOrange" x1="0" y1="0" x2="0" y2="1">
          <stop offset="0" stop-color="#ff4a00"/>
          <stop offset="0.6" stop-color="#ff8a10"/>
          <stop offset="1" stop-color="#ffb020"/>
        </linearGradient>
        <linearGradient id="crossScene" x1="0" y1="0" x2="0" y2="1">
          <stop offset="0" stop-color="#3d4a5a"/>
          <stop offset="0.5" stop-color="#8c8272"/>
          <stop offset="0.75" stop-color="#4a4035"/>
          <stop offset="1" stop-color="#0e0c0a"/>
        </linearGradient>
        <linearGradient id="greenSky" x1="0" y1="0" x2="1" y2="1">
          <stop offset="0" stop-color="#0f5a14"/>
          <stop offset="1" stop-color="#1c7a22"/>
        </linearGradient>
      </defs>

      <rect class="sky-photo" width="1090" height="398" fill="url(#skyBlue)" role="img" aria-label="Blue evening sky photograph"/>
      <polygon class="light-stripe" points="400,0 884,0 632,236" fill="#ffb866" opacity="0.8"/>
      <polygon class="sunset-photo" points="424,0 861,0 632,213" fill="url(#sunsetOrange)" role="img" aria-label="Orange sunset sky photograph"/>
      <polygon class="cross-photo" points="883,0 1090,207 1090,281 969,398 788,398 634,236" fill="url(#crossScene)" role="img" aria-label="Photograph of a cross silhouetted against a sunrise"/>
      <polygon class="green-photo" points="899,0 1090,0 1090,191" fill="url(#greenSky)" role="img" aria-label="Green-tinted sky photograph"/>
      <polygon class="white-divider" points="886,0 899,0 1090,191 1090,204" fill="#ffffff"/>
      <polygon class="orange-peak" points="788,398 883,331 969,398" fill="var(--brand-orange-warm)"/>
      <polygon class="orange-corner" points="1090,285 1090,398 969,398" fill="var(--brand-orange-warm)"/>
    </svg>

    <div class="headline-line headline-main headline-making">MAKING</div>
    <div class="headline-line headline-main headline-disciples">DISCIPLES</div>
    <div class="headline-line headline-sub headline-helping">&amp; HELPING THE</div>
    <div class="headline-line headline-sub headline-helpless">HELPLESS</div>
    <div class="tagline">For the Glory of Christ</div>

    <div class="footer-band">
      <div class="church-name"><span class="church-name-mark"></span>Merrow Fellowship Church</div>
      <div class="web-address">www.hfbmerrow.org</div>
    </div>
  </div>
</div>
</body>
</html>
```